Long term design collaboration - mobile app design & web app design

We are looking for a talented mobile designer to help us improve our UI & UX for mobile app and web app.

The screens that need to be redesigned are attached.

There is potentially a lot more work in future design available for the successful candidate.
The successful candidate would have to take part in daily stand-up around 3 times per week.
The successful candidate would join a dev team
We are software company that does property management

```html
<!DOCTYPE html>
<html lang="en">
<head>
<meta charset="utf-8">
<title>Development Overview</title>
<link href="https://fonts.googleapis.com/css2?family=Poppins:wght@400;500;600&display=swap" rel="stylesheet">
<style>
  :root {
    --bg: #f5f5fa;
    --surface: #ffffff;
    --title-blue: #2c5cc5;
    --ink: #1c1c22;
    --muted: #85858c;
    --tile-border: #e4e4ec;
    --accent: #f0a020;
    --accent-soft: #fdf0da;
    --alert: #d9822b;
  }
  * { box-sizing: border-box; margin: 0; padding: 0; }
  html, body { width: 1200px; height: 2602px; overflow: hidden; background: var(--bg); }
  body { font-family: 'Poppins', sans-serif; color: var(--ink); }
  .screen {
    position: absolute; left: 0; top: 0;
    width: 393px; height: 852px;
    transform: scale(3.0534); transform-origin: 0 0;
    background: var(--bg); overflow: hidden;
  }
  .app-bar {
    position: absolute; left: 0; top: 0; width: 393px; height: 74px;
    background: var(--surface);
    box-shadow: 0 2px 6px rgba(30,30,60,0.08);
  }
  .status-time { position: absolute; left: 14px; top: 12px; font-size: 12px; font-weight: 400; }
  .status-icons { position: absolute; right: 14px; top: 12px; display: flex; align-items: center; gap: 4px; font-size: 12px; }
  .back { position: absolute; left: 16px; top: 42px; }
  .page-title {
    position: absolute; left: 0; right: 0; top: 37px; text-align: center;
    color: var(--title-blue); font-size: 19px; font-weight: 600; letter-spacing: 0.1px;
  }
  .section {
    position: absolute; left: 20px; width: 353px;
    background: var(--surface); border-radius: 10px;
    box-shadow: 0 1px 6px rgba(30,30,60,0.07);
  }
  .section-title { position: absolute; left: 15px; top: 15px; font-size: 16px; font-weight: 500; }
  .tile {
    position: absolute; width: 153px; height: 94px;
    background: var(--surface); border: 1px solid var(--tile-border); border-radius: 6px;
    box-shadow: 0 1px 4px rgba(30,30,60,0.08);
    padding: 8px 30px 0 8px;
  }
  .tile-label { font-size: 13px; font-weight: 500; line-height: 18px; white-space: nowrap; }
  .tile-value { margin-top: 8px; font-size: 13px; color: var(--muted); line-height: 19px; white-space: nowrap; }
  .tile-value .status { color: var(--alert); font-weight: 500; }
  .tile-link { position: absolute; right: 10px; top: 9px; }
  .col-a { left: 15px; }
  .col-b { left: 185px; }
</style>
</head>
<body>
<div class="screen">
  <header class="app-bar">
    <div class="status-time">19:02</div>
    <div class="status-icons">
      <svg width="15" height="11" viewBox="0 0 15 11"><path d="M7.5 10.5 L1 4 A9.2 9.2 0 0 1 14 4 Z" fill="#1c1c22"/></svg>
      <span>100%</span>
      <svg width="24" height="11" viewBox="0 0 24 11"><rect x="0.5" y="0.5" width="20" height="10" rx="2.5" fill="none" stroke="#1c1c22"/><rect x="2" y="2" width="17" height="7" rx="1.2" fill="#1c1c22"/><rect x="21.5" y="3.5" width="1.6" height="4" rx="0.8" fill="#1c1c22"/></svg>
    </div>
    <svg class="back" width="14" height="18" viewBox="0 0 14 18"><path d="M10 2 L3 9 L10 16" fill="none" stroke="#1c1c22" stroke-width="2" stroke-linecap="round" stroke-linejoin="round"/></svg>
    <h1 class="page-title">Development Overview</h1>
  </header>

  <section class="section" style="top:113px;height:270px;">
    <h2 class="section-title">General</h2>
    <div class="tile col-a" style="top:51px;">
      <div class="tile-label">Handover Date</div>
      <div class="tile-value">12 January 2023</div>
      <svg class="tile-link" width="16" height="16" viewBox="0 0 16 16"><circle cx="8" cy="8" r="8" fill="var(--accent-soft)"/><path d="M5.5 10.5 L10.5 5.5 M6.5 5.5 H10.5 V9.5" fill="none" stroke="var(--accent)" stroke-width="1.4" stroke-linecap="round"/></svg>
    </div>
    <div class="tile col-b" style="top:51px;">
      <div class="tile-label">Units</div>
      <div class="tile-value">85</div>
      <svg class="tile-link" width="16" height="16" viewBox="0 0 16 16"><circle cx="8" cy="8" r="8" fill="var(--accent-soft)"/><path d="M5.5 10.5 L10.5 5.5 M6.5 5.5 H10.5 V9.5" fill="none" stroke="var(--accent)" stroke-width="1.4" stroke-linecap="round"/></svg>
    </div>
    <div class="tile col-a" style="top:162px;">
      <div class="tile-label">Address</div>
      <div class="tile-value">24 Marlow Grove Ave<br>London N7 3QP</div>
      <svg class="tile-link" width="16" height="16" viewBox="0 0 16 16"><circle cx="8" cy="8" r="8" fill="var(--accent-soft)"/><path d="M5.5 10.5 L10.5 5.5 M6.5 5.5 H10.5 V9.5" fill="none" stroke="var(--accent)" stroke-width="1.4" stroke-linecap="round"/></svg>
    </div>
    <div class="tile col-b" style="top:162px;">
      <div class="tile-label">Section 20 Limit</div>
      <div class="tile-value">£250</div>
    </div>
  </section>

  <section class="section" style="top:398px;height:381px;">
    <h2 class="section-title">Compliance</h2>
    <div class="tile col-a" style="top:51px;">
      <div class="tile-label">Asbestos</div>
      <div class="tile-value">N/A</div>
      <svg class="tile-link" width="16" height="16" viewBox="0 0 16 16"><circle cx="8" cy="8" r="8" fill="var(--accent-soft)"/><path d="M5.5 10.5 L10.5 5.5 M6.5 5.5 H10.5 V9.5" fill="none" stroke="var(--accent)" stroke-width="1.4" stroke-linecap="round"/></svg>
    </div>
    <div class="tile col-b" style="top:51px;">
      <div class="tile-label">EICR</div>
      <div class="tile-value">85</div>
      <svg class="tile-link" width="16" height="16" viewBox="0 0 16 16"><circle cx="8" cy="8" r="8" fill="var(--accent-soft)"/><path d="M5.5 10.5 L10.5 5.5 M6.5 5.5 H10.5 V9.5" fill="none" stroke="var(--accent)" stroke-width="1.4" stroke-linecap="round"/></svg>
    </div>
    <div class="tile col-a" style="top:162px;">
      <div class="tile-label">Drains</div>
      <div class="tile-value"><span class="status">Overdue</span><br>10 December 2023</div>
      <svg class="tile-link" width="16" height="16" viewBox="0 0 16 16"><circle cx="8" cy="8" r="8" fill="var(--accent-soft)"/><path d="M5.5 10.5 L10.5 5.5 M6.5 5.5 H10.5 V9.5" fill="none" stroke="var(--accent)" stroke-width="1.4" stroke-linecap="round"/></svg>
    </div>
    <div class="tile col-b" style="top:162px;">
      <div class="tile-label">Gutters</div>
      <div class="tile-value">N/A</div>
    </div>
    <div class="tile col-a" style="top:273px;">
      <div class="tile-label">Dry Risers</div>
      <div class="tile-value">N/A</div>
    </div>
  </section>

  <section class="section" style="top:795px;height:120px;">
    <h2 class="section-title">Insurance</h2>
    <div class="tile col-a" style="top:50px;"></div>
    <div class="tile col-b" style="top:50px;"></div>
  </section>
</div>
</body>
</html>
```